Business Card Design Project

Recently had a new logo made up for my company and new business cards done as well. I have attached the logos for your viewing. Additional projects may be needed. Good luck!

Industry/Entity Type

Business

```html
<!DOCTYPE html>
<html lang="en">
<head>
<meta charset="utf-8">
<title>Whitmore Financial Group – Business Cards</title>
<link rel="stylesheet" href="https://fonts.googleapis.com/css2?family=EB+Garamond:ital,wght@0,400;0,600;0,700;1,400&display=swap">
<style>
  :root {
    --page-bg: #e6e3de;
    --card-bg: #151515;
    --card-shadow: rgba(0,0,0,0.28);
    --gold: #c4ab6e;
    --silver: #cfcfcf;
    --white: #f4f4f2;
    --muted: #8e8a82;
    --frame-faint: #38352f;
  }
  * { margin: 0; padding: 0; box-sizing: border-box; }
  html, body { width: 1200px; height: 1000px; overflow: hidden; }
  body {
    background: var(--page-bg);
    font-family: "EB Garamond", Georgia, serif;
    position: relative;
  }
  .card {
    position: absolute;
    width: 660px;
    height: 377px;
    background: var(--card-bg);
    box-shadow: 0 14px 30px var(--card-shadow);
    overflow: hidden;
  }
  .card--front { left: 270px; top: 70px; }
  .card--back  { left: 270px; top: 540px; }

  /* faint decorative frames */
  .deco-frame {
    position: absolute;
    border: 12px solid var(--frame-faint);
  }
  .deco-frame--right { left: 470px; top: 40px; width: 170px; height: 210px; }
  .deco-frame--lower { left: 40px; top: 255px; width: 130px; height: 170px; }

  /* front: identity */
  .brand-block { position: absolute; left: 36px; top: 56px; width: 96px; }
  .brand-square {
    width: 52px; height: 52px;
    border: 2px solid var(--gold);
  }
  .brand-name {
    margin-top: 8px;
    font-size: 11px;
    letter-spacing: 1.5px;
    color: var(--gold);
    text-transform: uppercase;
    line-height: 1.25;
  }
  .person { position: absolute; left: 130px; top: 50px; }
  .person-name { font-size: 26px; font-weight: 700; color: var(--white); line-height: 1.1; }
  .person-title { font-size: 15px; font-style: italic; color: var(--gold); }
  .person-address { font-size: 13px; font-style: italic; color: var(--muted); line-height: 1.3; }

  .contact-box {
    position: absolute;
    left: 186px; top: 176px;
    width: 390px; height: 146px;
    border: 1.5px solid var(--gold);
    padding: 16px 22px;
    background: rgba(21,21,21,0.6);
  }
  .contact-line { font-size: 19px; font-weight: 600; color: var(--white); line-height: 1.4; white-space: nowrap; }
  .contact-label { display: inline-block; width: 20px; font-size: 13px; font-weight: 400; color: var(--muted); }

  /* back */
  .lockup {
    position: absolute; left: 96px; top: 142px;
    display: flex; align-items: center; gap: 14px;
  }
  .lockup-square { width: 40px; height: 40px; border: 2px solid var(--gold); flex: none; }
  .lockup-name { font-size: 22px; letter-spacing: 2px; color: var(--gold); text-transform: uppercase; white-space: nowrap; }
  .divider {
    position: absolute; left: 0; top: 200px;
    width: 660px; height: 1.5px; background: var(--silver);
  }
  .back-web {
    position: absolute; left: 150px; top: 226px;
    font-size: 30px; color: var(--gold); letter-spacing: 0.5px;
  }
</style>
</head>
<body>
  <section class="card card--front" aria-label="Business card front">
    <div class="deco-frame deco-frame--right"></div>
    <div class="deco-frame deco-frame--lower"></div>

    <div class="brand-block">
      <div class="brand-square"></div>
      <p class="brand-name">Whitmore Financial Group</p>
    </div>

    <div class="person">
      <p class="person-name">Daniel R. Whitmore</p>
      <p class="person-title">Estate Planning and Insurance Specialist</p>
      <p class="person-address">1420 Harbor View Road, Suite 310E<br>Maple Hollow, New York 10001</p>
    </div>

    <div class="contact-box">
      <p class="contact-line"><span class="contact-label">E:</span>dwhitmore@whitmorefinancial.com</p>
      <p class="contact-line"><span class="contact-label">P:</span>555-201-4830</p>
      <p class="contact-line"><span class="contact-label">F:</span>555-201-4831</p>
      <p class="contact-line"><span class="contact-label">W:</span>www.whitmorefinancial.com</p>
    </div>
  </section>

  <section class="card card--back" aria-label="Business card back">
    <div class="lockup">
      <div class="lockup-square"></div>
      <p class="lockup-name">Whitmore Financial Group</p>
    </div>
    <div class="divider"></div>
    <p class="back-web">www.whitmorefinancial.com</p>
  </section>
</body>
</html>
```